Icons for Workspaces for a financial CRM

We need several icons to indicate personal workspaces for different type of user(s) of our SaaS-based CRM.
We offer a front- and middle-office management software for the alternative assets industry - private equity, hedge funds, real estate, institutional investors, etc - thourgh our proprietary software called Veltrix. The company's main office is in Boston.
The workspaces in question represent personalized Home pages, based on the user persona - there is a workspace for Investor Relations people, another for Deal Management people, etc. There is also a "My Home" workspace where the user can arrange their own informatation. One user can have access to sevaral workspaces, they are not limited to just one.
The buttons that will point the user the workspaces, will be placed on top left position of the screen, one under the other, as a list. The icons will be coupled with text.
Here is the list of all workspaces for which we need icons - a total of 8 icons (with explanations):
• My Home
(personalized home workspace for the logged in user)
• Fundraising
Raising money for a fund.
• Investor Relations
The management of existing client relationships
• Deal Management
The management of new investments
• Portfolio Management
The management of existing investments
• Research Management
The gathering of information about the market, industry trends, innovations, etc.
• Resource Management
The management of people resources
• Portal Management
Managing of user accounts for our investor portal. This is setting up new users, editing existing users, and deactivating prior users.
The default colors of the Veltrix application are light-blue and light-grey, but we also provide different skins, so it will be good to see a couple of versions, in different colors.
Size - 32 x 32 pixels
Target Market(s)
People who work in the financial industry.
Industry/Entity Type
Financial

```html
<!DOCTYPE html>
<html lang="en">
<head>
<meta charset="utf-8">
<title>Workspaces</title>
<link rel="stylesheet" href="https://fonts.googleapis.com/css2?family=Arimo:wght@400;700&display=swap">
<style>
  :root {
    --page-bg: #f2f2f2;
    --sidebar-top: #ececec;
    --sidebar-bottom: #e2e2e2;
    --sidebar-shadow: rgba(0, 0, 0, 0.28);
    --nav-text: #444444;
    --title-text: #555555;
    --body-text: #555555;
    --icon-home: #c9c9c9;
    --icon-home-roof: #c0392b;
    --icon-coins: #d9a514;
    --icon-people: #c58a3e;
    --icon-deal: #8c9196;
    --icon-portfolio: #6b3f22;
    --icon-research: #3a9a3a;
    --icon-resource: #5b7fb8;
    --icon-portal: #4a76c7;
  }
  * { margin: 0; padding: 0; box-sizing: border-box; }
  html, body { width: 1200px; height: 1200px; overflow: hidden; }
  body {
    position: relative;
    background: var(--page-bg);
    font-family: "Arimo", Arial, sans-serif;
  }
  .sidebar {
    position: absolute;
    left: 0; top: 0;
    width: 504px; height: 1200px;
    background: linear-gradient(180deg, var(--sidebar-top), var(--sidebar-bottom));
    box-shadow: 6px 0 14px var(--sidebar-shadow);
    z-index: 2;
  }
  .workspace-list { list-style: none; padding-top: 24px; }
  .workspace-item {
    display: flex;
    align-items: center;
    height: 120px;
    padding-left: 29px;
  }
  .workspace-icon {
    width: 72px; height: 72px;
    flex: none;
    border-radius: 10px;
    margin-right: 26px;
  }
  .icon-home { background: linear-gradient(180deg, var(--icon-home-roof) 0 30%, var(--icon-home) 30%); }
  .icon-fundraising { background: radial-gradient(circle at 50% 55%, #f3d35c, var(--icon-coins)); }
  .icon-investors { background: linear-gradient(90deg, var(--icon-people), #2f5fa8); }
  .icon-deals { background: linear-gradient(180deg, #e8e8e8, var(--icon-deal)); }
  .icon-portfolio { background: linear-gradient(180deg, #8a5631, var(--icon-portfolio)); }
  .icon-research { background: radial-gradient(circle at 40% 45%, #7bd35a, var(--icon-research)); }
  .icon-resource { background: linear-gradient(135deg, #9aa9c4, var(--icon-resource)); }
  .icon-portal { background: linear-gradient(135deg, var(--icon-portal) 0 50%, #e07a24 50%); }
  .workspace-label {
    font-size: 29px;
    font-weight: 700;
    color: var(--nav-text);
  }
  .content {
    position: absolute;
    left: 552px; top: 36px;
    width: 800px;
    color: var(--body-text);
  }
  .content-title {
    font-size: 41px;
    font-weight: 700;
    color: var(--title-text);
    margin-bottom: 26px;
  }
  .content p {
    font-size: 29px;
    line-height: 49px;
    margin-bottom: 53px;
  }
</style>
</head>
<body>
  <nav class="sidebar">
    <ul class="workspace-list">
      <li class="workspace-item"><span class="workspace-icon icon-home" role="img" aria-label="House icon"></span><span class="workspace-label">Home</span></li>
      <li class="workspace-item"><span class="workspace-icon icon-fundraising" role="img" aria-label="Stacks of gold coins icon"></span><span class="workspace-label">Fundraising</span></li>
      <li class="workspace-item"><span class="workspace-icon icon-investors" role="img" aria-label="Two business people icon"></span><span class="workspace-label">Investor Relations</span></li>
      <li class="workspace-item"><span class="workspace-icon icon-deals" role="img" aria-label="Contract documents icon"></span><span class="workspace-label">Deal Management</span></li>
      <li class="workspace-item"><span class="workspace-icon icon-portfolio" role="img" aria-label="Brown briefcase icon"></span><span class="workspace-label">Portfolio Management</span></li>
      <li class="workspace-item"><span class="workspace-icon icon-research" role="img" aria-label="Green and blue pie chart icon"></span><span class="workspace-label">Research Management</span></li>
      <li class="workspace-item"><span class="workspace-icon icon-resource" role="img" aria-label="Stacked profile cards icon"></span><span class="workspace-label">Resource Management</span></li>
      <li class="workspace-item"><span class="workspace-icon icon-portal" role="img" aria-label="Four coloured window tiles icon"></span><span class="workspace-label">Portal Management</span></li>
    </ul>
  </nav>
  <main class="content">
    <h1 class="content-title">Phasellus vel scelerisque eros</h1>
    <p>Phasellus vel scelerisque eros. In vitae diam felis. Sed tincidunt nisi ut erat eleifend vitae fringilla nibh adipiscing. Phasellus et leo ante. Sed mauris massa, ultrices a sollicitudin vel, mattis id dolor. Mauris a velit lectus. Morbi ac tempus magna. Nunc lorem augue, tristique placerat vel, accumsan vitae orci. Aenean quis consequat erat. Nam elit eros, laoreet vitae laoreet a, sagittis vel metus. Nulla adipiscing volutpat consequat. Integer aliquet ante et magna feugiat nec faucibus lorem eleifend. Phasellus et mi sed quam pharetra placerat ut sit amet elit. Sed nisi justo, tempus nec vestibulum ut, dignissim non orci.</p>
    <p>Donec a nunc orci, vitae fermentum urna. Sed scelerisque accumsan odio, aliquet sollicitudin ligula tristique at. Sed gravida cursus tincidunt. Sed condimentum, nunc faucibus accumsan sodales, ante augue euismod tellus, ac auctor lorem dui id purus. Fusce facilisis tellus eu nunc pulvinar non aliquam enim rutrum. Praesent massa leo, vestibulum a fermentum nec, cursus quis libero. Vestibulum ante ipsum primis in faucibus orci luctus et ultrices posuere cubilia Curae; Curabitur vel.</p>
  </main>
</body>
</html>
```